Flyer

I am a qualified accountant and I need a flyer to promote my business when networking

My services include
Management Accounts, Financial Accounts, Day to Day Bookkeeping services, business start up assistance
I will produce and submit Self Assessment Tax Returns, Annual Accounts, VAT tax returns, Payroll and PAYE

I attach my business card design so that there is some continuity if you think it appropiate.

Size A3 is preferred, please.

Sorry, I mean't Size A5 is preferred.

A5 please

Free initial consultations and advice.                                   

Business

```html
<!DOCTYPE html>
<html lang="en">
<head>
<meta charset="utf-8">
<title>Clare Whitby Accounting – Flyer</title>
<link rel="stylesheet" href="https://fonts.googleapis.com/css2?family=Cinzel:wght@400&family=Montserrat:wght@500&family=Oswald:wght@500&family=Roboto+Condensed:wght@300;700&display=swap">
<style>
  :root {
    --page-bg: #e4e4e4;
    --lime-light: #c3dc38;
    --green-body: #93c84c;
    --lime-arc: #b9d936;
    --lime-footer: #a9d03c;
    --ribbon-top: #2aa3d6;
    --ribbon-bottom: #1479ac;
    --white: #ffffff;
    --ink: #2b2b2b;
    --photo-light: #eef1f4;
    --photo-mid: #c9d3dd;
  }
  * { box-sizing: border-box; margin: 0; padding: 0; }
  html, body {
    width: 1200px; height: 1200px; overflow: hidden;
    background: var(--page-bg);
  }
  .flyer {
    position: absolute; left: 228px; top: 72px;
    width: 744px; height: 1056px;
    background: var(--green-body);
    overflow: hidden;
  }
  .header-band {
    position: absolute; left: 0; top: 0; width: 100%; height: 120px;
    background: var(--lime-light);
    border-bottom: 3px solid var(--white);
  }
  .owner-title {
    position: absolute; left: 0; top: 30px; width: 100%;
    text-align: center; color: var(--white);
    font-family: "Cinzel", serif; font-weight: 400;
    font-size: 53px; line-height: 1; letter-spacing: 1px;
  }
  .owner-title .credentials { font-size: 38px; }
  .ribbon {
    position: absolute; left: 124px; top: 110px; width: 496px; height: 56px;
  }
  .ribbon-label {
    position: absolute; left: 0; top: 5px; width: 100%; height: 56px;
    display: flex; align-items: center; justify-content: center;
    font-family: "Oswald", sans-serif; font-weight: 500;
    font-size: 32px; color: var(--white); letter-spacing: 0.5px;
  }
  .services {
    position: absolute; left: 0; top: 182px; width: 100%;
    text-align: center; list-style: none; color: var(--white);
    font-family: "Montserrat", sans-serif; font-weight: 500;
    font-size: 31px; line-height: 36px;
  }
  .submission-heading {
    position: absolute; left: 0; top: 342px; width: 100%;
    text-align: center; color: var(--white);
    font-family: "Roboto Condensed", sans-serif; font-weight: 700;
    font-size: 32px; line-height: 40px;
  }
  .submission-list {
    position: absolute; left: 0; top: 381px; width: 100%;
    text-align: center; list-style: none; color: var(--white);
    font-family: "Roboto Condensed", sans-serif; font-weight: 300;
    font-size: 26px; line-height: 30px;
  }
  .team-photo {
    position: absolute; left: 0; top: 770px; width: 100%; height: 210px;
    background: linear-gradient(100deg, var(--photo-mid) 0%, var(--photo-light) 35%, var(--photo-mid) 60%, var(--photo-light) 100%);
  }
  .curves {
    position: absolute; left: 0; top: 0; width: 744px; height: 1056px;
  }
  .brand {
    position: absolute; left: 0; top: 640px; width: 100%;
    display: flex; align-items: center; justify-content: center; gap: 14px;
  }
  .brand-dot {
    width: 30px; height: 30px; border-radius: 50%;
    background: var(--lime-arc);
  }
  .business-name {
    color: var(--ink);
    font-family: "Montserrat", sans-serif; font-weight: 500;
    font-size: 26px; line-height: 36px;
  }
  .tagline {
    position: absolute; left: 0; top: 680px; width: 100%;
    text-align: center; color: var(--ink);
    font-family: "Montserrat", sans-serif; font-weight: 500;
    font-size: 16px; line-height: 24px;
  }
  .contact {
    position: absolute; left: 0; top: 770px; width: 100%;
    text-align: center; color: var(--ink);
    font-family: "Montserrat", sans-serif; font-weight: 500;
  }
  .contact .email { font-size: 20px; line-height: 32px; }
  .contact .phone { font-size: 27px; line-height: 36px; letter-spacing: 1px; }
  .footer-band {
    position: absolute; left: 0; top: 980px; width: 100%; height: 76px;
    background: var(--lime-footer);
    border-top: 3px solid var(--lime-light);
    display: flex; align-items: center; justify-content: center;
    color: var(--white);
    font-family: "Montserrat", sans-serif; font-weight: 500; font-size: 32px;
  }
</style>
</head>
<body>
  <main class="flyer">
    <div class="header-band"></div>
    <h1 class="owner-title">Clare Whitby <span class="credentials">ACMA, CGMA</span></h1>

    <div class="ribbon">
      <svg width="496" height="56" viewBox="0 0 496 56" aria-hidden="true">
        <defs>
          <linearGradient id="ribbonFill" x1="0" y1="0" x2="0" y2="1">
            <stop offset="0" stop-color="var(--ribbon-top)"/>
            <stop offset="1" stop-color="var(--ribbon-bottom)"/>
          </linearGradient>
        </defs>
        <path d="M0,10 L496,10 L484,56 L12,56 Z" fill="url(#ribbonFill)"/>
        <path d="M0,10 L496,10 L496,14 L0,14 Z" fill="#0f5f8a" opacity="0.5"/>
      </svg>
      <div class="ribbon-label">SERVICES OFFERED</div>
    </div>

    <ul class="services">
      <li>Management Accounts</li>
      <li>Financial Accounts</li>
      <li>Day to Day Bookkeeping services</li>
      <li>Business Start Up Assistance</li>
    </ul>

    <h2 class="submission-heading">Production and submission of:</h2>
    <ul class="submission-list">
      <li>Self Assessment Tax Returns</li>
      <li>VAT returns</li>
      <li>Annual Accounts</li>
      <li>Payroll &amp; PAYE</li>
      <li>I also offer business start up assitance</li>
    </ul>

    <div class="team-photo" role="img" aria-label="Photo of business people meeting around a table with a laptop and paperwork"></div>

    <svg class="curves" viewBox="0 0 744 1056" aria-hidden="true">
      <path d="M0,628 Q372,500 744,628 L744,654 Q372,540 0,654 Z" fill="var(--lime-arc)"/>
      <path d="M0,654 Q372,540 744,654 L744,770 Q372,912 0,770 Z" fill="var(--white)"/>
      <path d="M0,770 Q372,912 744,770 L744,778 Q372,930 0,778 Z" fill="var(--lime-arc)"/>
    </svg>

    <div class="brand">
      <span class="brand-dot" aria-hidden="true"></span>
      <p class="business-name">Clare Whitby Accounting</p>
    </div>
    <p class="tagline">Making Accounts look easy</p>

    <div class="contact">
      <p class="email">clare@clarewhitbyaccounting.com</p>
      <p class="phone">07700 900123</p>
    </div>

    <p class="footer-band">Free initial consultations and advice.</p>
  </main>
</body>
</html>
```